Glanvero foot health or foot health glanvero

Treatments in comfort of your own home
Delia Marsh cert KTRVb Pod, LQNDoct
Treatments will be listed on the leaflet I will attach
I am a Foot Health practitioner,
I want to mention I do home visits throughout Pembrokeshire & Ceredigion.
Tel. 07604519283
I have 2 logs to forward to you they are the associations I belong to .
One of which is also a certification mark. It is important that the same colour is used for this mark. They are not the main focus, they are just recognised mark. To be at the top or bottom of the page.
There is a local business called Tregarrow foot clinic, so my business has to be glanvero foot health, or foot health glanvero
soon I will also need a web page and cards designed, so please keep this in mind when designing the Artwork. I will also need an email on the leaflet but I will wait and see what the design is first before I confirm it as I have several.
I hope this is enough info for you.
Many thanks,
Delia Marsh

Target Market(s)

Mostly the elderly, some middle age women, but it is a service for all ages. The elderly are my main clients.

Industry/Entity Type

Health

Font styles to use
Serif
Sans Serif

Colors

Designer to choose colors to be used in the design.

Requirements
Must have
• Covering Pembrokeshire & Ceredigion.
Treatments include:- as listed on example leaflet I sent
Phone number a size that's easily readable.
I am open to colours. I love bright colours, but also like the more conservative colours as long as it looks professional. I'm wanting it to look more up market.
Nice to have
• Logo for Guildhall and KTE logo obviously smaller, but also recognisable and either at the top of page or bottom. These are not to be main focal point.

```html
<!DOCTYPE html>
<html lang="en">
<head>
<meta charset="utf-8">
<title>Glanvero Foot Health Specialist</title>
<link rel="stylesheet" href="https://fonts.googleapis.com/css2?family=Arimo:wght@700&family=Josefin+Sans:wght@600&family=Poiret+One&family=Tinos&display=swap">
<style>
  :root {
    --page: #ffffff;
    --deep-teal: #0f4a5c;
    --mid-teal: #2c7f8c;
    --aqua: #4fb3ad;
    --stripe-top: #3fae6a;
    --stripe-bottom: #6fd6c4;
    --drop-blue: #3a8fc8;
    --drop-dark: #123f66;
    --accent-yellow: #f3ea72;
    --ink: #050505;
    --white: #ffffff;
    --badge-dark: rgba(10, 30, 36, 0.82);
    --seal: rgba(255, 255, 255, 0.88);
    --band: #000000;
  }
  * { box-sizing: border-box; margin: 0; padding: 0; }
  html, body {
    width: 1200px; height: 1200px; overflow: hidden;
    background: var(--page);
  }
  .leaflet {
    position: absolute; left: 207px; top: 48px;
    width: 776px; height: 1100px; overflow: hidden;
    background:
      radial-gradient(ellipse 70% 45% at 35% 35%, rgba(79,179,173,0.55), transparent 70%),
      linear-gradient(160deg, var(--deep-teal) 0%, var(--mid-teal) 45%, var(--aqua) 85%, #5cc2b6 100%);
  }
  .side-stripe {
    position: absolute; right: 0; top: 0; width: 101px; height: 1014px;
    background: linear-gradient(180deg, var(--stripe-top) 0%, #56c6a6 45%, var(--stripe-bottom) 100%);
    opacity: 0.9;
  }
  .association-marks {
    position: absolute; right: 20px; top: 26px; width: 62px;
    display: flex; flex-direction: column; gap: 14px;
  }
  .association-mark {
    width: 62px; height: 62px; border-radius: 50%;
    background: var(--seal);
  }
  .footprint-visual {
    position: absolute; left: 33px; top: 400px; width: 645px; height: 512px;
    background:
      radial-gradient(ellipse 22% 18% at 18% 18%, var(--drop-blue), transparent 75%),
      radial-gradient(ellipse 22% 16% at 28% 86%, var(--drop-blue), transparent 75%),
      radial-gradient(ellipse 40% 12% at 40% 6%, rgba(58,143,200,0.6), transparent 75%),
      radial-gradient(ellipse 30% 16% at 82% 72%, rgba(58,143,200,0.6), transparent 75%),
      radial-gradient(ellipse 60% 60% at 45% 50%, rgba(18,63,102,0.35), transparent 80%);
  }
  .brand-name {
    position: absolute; left: 112px; top: 37px; width: 296px; height: 70px;
    background: var(--badge-dark);
    display: flex; align-items: center; justify-content: center;
    font-family: "Josefin Sans", sans-serif; font-weight: 600;
    font-size: 50px; color: var(--white); letter-spacing: 1px;
  }
  .brand-tagline {
    position: absolute; left: 55px; top: 120px; width: 408px; height: 50px;
    background: var(--badge-dark);
    display: flex; align-items: center; justify-content: center;
    font-family: "Poiret One", sans-serif; font-size: 36px; color: #d8dede;
  }
  .headline {
    position: absolute; left: 0; width: 718px; top: 222px; text-align: center;
    font-family: "Poiret One", sans-serif; font-weight: 400;
    font-size: 46px; color: var(--accent-yellow); letter-spacing: 1px;
    -webkit-text-stroke: 0.8px var(--accent-yellow);
  }
  .practitioner {
    position: absolute; left: 0; width: 718px; top: 276px; text-align: center;
    font-family: "Arimo", sans-serif; font-weight: 700;
    font-size: 25px; letter-spacing: 0.5px; color: var(--white);
  }
  .treatments-title {
    position: absolute; left: 0; width: 790px; top: 362px; text-align: center;
    font-family: "Poiret One", sans-serif; font-size: 40px;
    color: var(--accent-yellow); text-decoration: underline;
    text-underline-offset: 4px; -webkit-text-stroke: 0.6px var(--accent-yellow);
  }
  .treatment-list { list-style: none; }
  .treatment {
    position: absolute;
    font-family: "Arimo", sans-serif; font-weight: 700;
    font-size: 27px; letter-spacing: 1px; white-space: nowrap;
  }
  .treatment--dark { left: 285px; color: var(--ink); }
  .treatment--light { right: 44px; color: var(--accent-yellow); }
  .coverage {
    position: absolute; left: 0; width: 718px; top: 934px; text-align: center;
    font-family: "Tinos", serif; font-size: 30px; color: var(--white);
  }
  .contact-band {
    position: absolute; left: 0; bottom: 0; width: 776px; height: 86px;
    background: var(--band); text-align: center; color: var(--accent-yellow);
  }
  .contact-phone {
    display: block; margin-top: 8px;
    font-family: "Josefin Sans", sans-serif; font-weight: 600; font-size: 32px;
  }
  .contact-note {
    display: block; margin-top: 2px;
    font-family: "Tinos", serif; font-size: 19px;
  }
</style>
</head>
<body>
  <main class="leaflet">
    <div class="side-stripe"></div>
    <div class="association-marks">
      <div class="association-mark" role="img" aria-label="Professional association mark"></div>
      <div class="association-mark" role="img" aria-label="Certification mark"></div>
    </div>
    <div class="footprint-visual" role="img" aria-label="Water droplets on glass forming two footprints"></div>

    <h1 class="brand-name">Glanvero</h1>
    <p class="brand-tagline">Foot Health Specialist</p>

    <h2 class="headline">COMPREHENSIVE FOOT CARE</h2>
    <p class="practitioner">DELIA MARSH KTRVb, LQNDoct(FHP)</p>

    <h3 class="treatments-title">TREATMENTS INCLUDE</h3>
    <ul class="treatment-list">
      <li class="treatment treatment--dark" style="top:439px">DIABETIC FOOT CARE</li>
      <li class="treatment treatment--light" style="top:493px">INGROWING TOENAILS</li>
      <li class="treatment treatment--dark" style="top:554px">CORN &amp; CALLOUS TREATMENT</li>
      <li class="treatment treatment--light" style="top:614px">TOENAIL CLIPPING</li>
      <li class="treatment treatment--dark" style="top:677px">FUNGAL INFECTIONS TREATED</li>
      <li class="treatment treatment--light" style="top:731px">CRACKED HEELS</li>
    </ul>

    <p class="coverage">Covering Pembrokeshire &amp; Ceredigion</p>

    <footer class="contact-band">
      <span class="contact-phone">07604-519283</span>
      <span class="contact-note">Home visits by arrangement</span>
    </footer>
  </main>
</body>
</html>
```